Sickle Cell Patient Flyer

I need this be appealing to families dealing with sickle cell disease. Both informative-introducing the idea that a stroke prevention program is not only easy for their children but necessary. Stroke is a risk to all with children with SCD.
I included a few info flyers from the Brainward Alliance and licensed to me photos I like. I am open to suggestions.
web address is carebrightpath.example
Call to schedule 855-555-0148
TCD is a safe and accurate tool that makes stroke prevention possible for your SCD patients and family.
Risk is highest for SCD sufferers age 2 to 5. Protect your childs future.

Target Market(s)

Parents, families and medical professionals

Industry/Entity Type

Medical wellness

Font styles to use
Other font styles liked:
• something close to my logo font

Colors
0094D4
00A9DD
6FCCEA
C7EBF8
E9F6FB

Requirements
Nice to have
• pictures of kids (Children of color) pictures of Brains, kids happy with medical professionals
Should not have
• dark colors

```html
<!DOCTYPE html>
<html lang="en">
<head>
<meta charset="utf-8">
<title>Stroke Prevention for Children with Sickle Cell Disease – Flyer</title>
<link rel="stylesheet" href="https://fonts.googleapis.com/css2?family=Roboto+Condensed:wght@500;700;800&family=Montserrat:wght@500;600;700&display=swap">
<style>
  :root{
    --blue:#0094D4;
    --blue-mid:#00A9DD;
    --blue-soft:#6FCCEA;
    --blue-pale:#C7EBF8;
    --blue-mist:#E9F6FB;
    --navy-blue:#1B6FB8;
    --green:#5DB79A;
    --green-deep:#3E9E80;
    --green-photo:#7FC2A6;
    --white:#FFFFFF;
    --stage:#EEF1F3;
  }
  *{box-sizing:border-box;margin:0;padding:0}
  html,body{width:1200px;height:2456px;overflow:hidden}
  body{background:var(--stage);font-family:"Montserrat",Arial,sans-serif;position:relative}

  .flyer{position:absolute;left:50px;top:488px;width:1100px;height:1480px;background:var(--white);overflow:hidden;box-shadow:0 10px 40px rgba(0,60,100,.12)}

  /* header */
  .hero{position:absolute;left:0;top:0;width:1100px;height:600px}
  .hero-photo{position:absolute;left:560px;top:0;width:540px;height:600px;background:radial-gradient(circle at 55% 35%,#9ED3BC 0%,var(--green-photo) 55%,#5FAE8F 100%)}
  .brand{position:absolute;left:50px;top:46px;display:flex;align-items:center;gap:14px}
  .brand-mark{width:26px;height:26px;background:var(--green)}
  .brand-name{font-family:"Roboto Condensed",Arial,sans-serif;font-weight:800;font-size:40px;color:var(--navy-blue);letter-spacing:.5px}
  .hero-band{position:absolute;left:0;top:220px;width:560px;height:16px;background:var(--blue-soft)}
  .headline{position:absolute;left:50px;top:262px;width:500px;font-family:"Roboto Condensed",Arial,sans-serif;font-weight:800;font-size:58px;line-height:1.04;color:var(--navy-blue)}
  .headline .accent{color:var(--green);display:block}

  /* key facts */
  .facts{position:absolute;left:0;top:600px;width:1100px;height:560px;background:linear-gradient(180deg,var(--blue-soft) 0%,var(--blue-mid) 100%)}
  .facts-tab{position:absolute;left:420px;top:0;width:260px;height:70px;background:var(--blue);color:var(--white);font-family:"Roboto Condensed",Arial,sans-serif;font-weight:700;font-size:36px;display:flex;align-items:center;justify-content:center;letter-spacing:1px}
  .fact-list{position:absolute;left:70px;top:110px;width:960px;display:flex;gap:32px}
  .fact{width:216px;height:400px;background:var(--green);clip-path:polygon(0 0,100% 0,100% 88%,50% 100%,0 88%);padding:28px 20px 0;text-align:center;color:var(--white)}
  .fact-icon{width:84px;height:84px;margin:0 auto 22px;border:3px solid var(--white);border-radius:50%;display:flex;align-items:center;justify-content:center}
  .fact p{font-size:17px;line-height:1.4;font-weight:500}

  /* message */
  .message{position:absolute;left:0;top:1160px;width:1100px;height:240px}
  .protect{position:absolute;left:50px;top:48px;width:330px;font-family:"Roboto Condensed",Arial,sans-serif;font-weight:800;font-size:44px;line-height:1.05;color:var(--blue)}
  .divider{position:absolute;left:400px;top:48px;width:3px;height:140px;background:var(--blue-pale)}
  .claim{position:absolute;left:430px;top:52px;width:620px;font-family:"Roboto Condensed",Arial,sans-serif;font-weight:700;font-size:26px;line-height:1.25;color:var(--navy-blue)}
  .risk{position:absolute;left:430px;top:160px;font-family:"Roboto Condensed",Arial,sans-serif;font-weight:700;font-size:24px;color:var(--blue)}
  .contact-tab{position:absolute;right:40px;bottom:0;padding:12px 26px;background:var(--blue);color:var(--white);font-family:"Roboto Condensed",Arial,sans-serif;font-weight:700;font-size:20px;letter-spacing:1px}

  /* footer */
  .footer{position:absolute;left:0;top:1400px;width:1100px;height:80px;background:var(--blue-mist);border-top:6px solid var(--blue);display:flex;align-items:center;justify-content:space-around;padding:0 30px}
  .footer-item{display:flex;align-items:center;gap:10px;font-size:18px;font-weight:600;color:var(--navy-blue)}
  .footer-item svg{flex:none}
</style>
</head>
<body>
<main class="flyer">
  <header class="hero">
    <div class="brand">
      <span class="brand-mark"></span>
      <span class="brand-name">CareBright Path</span>
    </div>
    <div class="hero-band"></div>
    <h1 class="headline">Stroke Prevention for Children with <span class="accent">sickle cell disease is possible!</span></h1>
    <div class="hero-photo" role="img" aria-label="Photo of a smiling schoolboy pointing up at line drawings of a brain on a green background"></div>
  </header>

  <section class="facts">
    <h2 class="facts-tab">KEY FACTS</h2>
    <div class="fact-list">
      <article class="fact">
        <div class="fact-icon"><svg width="44" height="44" viewBox="0 0 44 44" fill="none" stroke="#fff" stroke-width="3"><circle cx="22" cy="22" r="16"/><path d="M22 12v11l7 5"/></svg></div>
        <p>About 11% of SCD patients have a stroke before age 20, with the highest risk between age 2 and 5.</p>
      </article>
      <article class="fact">
        <div class="fact-icon"><svg width="44" height="44" viewBox="0 0 44 44" fill="none" stroke="#fff" stroke-width="3"><path d="M4 24h8l4-10 6 20 5-14 3 4h10"/></svg></div>
        <p>Our screening uses ultrasound, which is transcranial doppler.</p>
      </article>
      <article class="fact">
        <div class="fact-icon"><svg width="44" height="44" viewBox="0 0 44 44" fill="none" stroke="#fff" stroke-width="3"><path d="M22 38s-14-8-14-19a8 8 0 0 1 14-5 8 8 0 0 1 14 5c0 11-14 19-14 19z"/></svg></div>
        <p>Simple and painless screening for your child.</p>
      </article>
      <article class="fact">
        <div class="fact-icon"><svg width="44" height="44" viewBox="0 0 44 44" fill="none" stroke="#fff" stroke-width="3"><path d="M22 5l14 6v10c0 9-6 15-14 18C14 36 8 30 8 21V11z"/><path d="M15 22l5 5 9-10"/></svg></div>
        <p>Screening finds early signs of stroke, allowing treatments that lower the risk.</p>
      </article>
    </div>
  </section>

  <section class="message">
    <h2 class="protect">PROTECT YOUR CHILDS FUTURE</h2>
    <div class="divider"></div>
    <p class="claim">TCD IS A SAFE &amp; ACCURATE TOOL THAT MAKES STROKE PREVENTION POSSIBLE FOR YOUR SCD PATIENTS AND FAMILY.</p>
    <p class="risk">RISK IS HIGHEST FOR SCD SUFFERERS AGE 2 TO 5.</p>
    <div class="contact-tab">CONTACT US</div>
  </section>

  <footer class="footer">
    <span class="footer-item"><svg width="22" height="22" viewBox="0 0 24 24" fill="#0094D4"><path d="M6.6 10.8a15 15 0 0 0 6.6 6.6l2.2-2.2a1 1 0 0 1 1-.25 11.4 11.4 0 0 0 3.6.57 1 1 0 0 1 1 1V20a1 1 0 0 1-1 1A17 17 0 0 1 3 4a1 1 0 0 1 1-1h3.5a1 1 0 0 1 1 1c0 1.25.2 2.45.57 3.6a1 1 0 0 1-.25 1z"/></svg>855-555-0148</span>
    <span class="footer-item"><svg width="22" height="22" viewBox="0 0 24 24" fill="none" stroke="#0094D4" stroke-width="2"><rect x="3" y="5" width="18" height="14" rx="1"/><path d="M3 6l9 7 9-7"/></svg>info@carebrightpath.example</span>
    <span class="footer-item"><svg width="22" height="22" viewBox="0 0 24 24" fill="none" stroke="#0094D4" stroke-width="2"><circle cx="12" cy="12" r="9"/><path d="M3 12h18M12 3c3 3 3 15 0 18M12 3c-3 3-3 15 0 18"/></svg>www.carebrightpath.example</span>
  </footer>
</main>
</body>
</html>
```